Managed WIFI Solutions A5

Hi, We are looking for a flyer to present to our client list (mainly Hospitality clients like restaurants) to offer then managed Wireless Network Solutions.

We offer guest and private Wireless network solutions. The Restaurant has the choice of how they want to set it up.

This will allow the restaurants to offer their clients Free wifi without effecting their own Wifi network.

I have attached out logo for you to incorporate.

I think an A5 is the best size, But i am open to suggestions.

Industry/Entity Type

Hospitality

Requirements
Must have
• Emphasis on Managed WIFI.
Nice to have
• Coffee shop theme. So maybe someone on a laptop in the background

```html
<!DOCTYPE html>
<html lang="en">
<head>
<meta charset="utf-8">
<title>Harborline Managed WiFi Flyer</title>
<link rel="stylesheet" href="https://fonts.googleapis.com/css2?family=Oswald:wght@400;500;600;700&family=Open+Sans:wght@400;600;700&display=swap">
<style>
  :root {
    --orange: #f39a1e;
    --black: #1b1b1b;
    --white: #ffffff;
    --text: #3a3a3a;
    --brand-ink: #2b2b2b;
    --backdrop: #d9d9d9;
  }
  * { box-sizing: border-box; margin: 0; padding: 0; }
  html, body { width: 1200px; height: 800px; overflow: hidden; }
  body {
    background: var(--backdrop);
    font-family: "Open Sans", Arial, sans-serif;
    position: relative;
  }
  .flyer {
    position: absolute;
    top: 117px;
    width: 400px;
    height: 566px;
    background: var(--white);
    overflow: hidden;
    box-shadow: 0 6px 18px rgba(0,0,0,.18);
  }
  .flyer--front { left: 170px; }
  .flyer--back { left: 630px; }

  /* Front */
  .brand {
    position: absolute;
    top: 44px;
    right: 28px;
    display: flex;
    align-items: baseline;
    gap: 14px;
  }
  .brand__name {
    font-family: "Oswald", sans-serif;
    font-weight: 500;
    font-size: 24px;
    line-height: 1;
    letter-spacing: 1px;
    color: var(--brand-ink);
    text-transform: uppercase;
  }
  .brand__partner {
    font-family: "Oswald", sans-serif;
    font-weight: 500;
    font-size: 12px;
    line-height: 1;
    color: var(--brand-ink);
  }
  .front__rule {
    position: absolute;
    top: 102px; left: 0;
    width: 100%; height: 8px;
    background: var(--orange);
  }
  .front__photo {
    position: absolute;
    top: 110px; left: 0;
    width: 100%; height: 456px;
    background:
      linear-gradient(180deg, rgba(0,0,0,0) 55%, rgba(120,72,30,.85) 100%),
      linear-gradient(90deg, #e8e4dc 0%, #bfb6a8 14%, #4a4a4c 26%, #3a3a3c 60%, #2f2f31 100%);
  }
  .front__headline {
    position: absolute;
    top: 232px;
    right: 34px;
    text-align: right;
    font-family: "Oswald", sans-serif;
    font-weight: 600;
    text-transform: uppercase;
    line-height: 1.02;
  }
  .front__headline span { display: block; }
  .headline__offer { font-size: 40px; color: var(--white); }
  .headline__audience { font-size: 27px; color: var(--white); }
  .headline__wifi { font-size: 40px; color: var(--orange); }

  /* Back */
  .back__shapes { position: absolute; inset: 0; }
  .back__intro {
    position: absolute;
    top: 22px; left: 26px; right: 26px;
    color: var(--white);
    font-size: 9.5px;
    line-height: 1.35;
  }
  .back__title {
    display: block;
    font-family: "Oswald", sans-serif;
    font-weight: 700;
    font-size: 22px;
    line-height: 1;
    color: var(--orange);
    margin-bottom: 4px;
  }
  .checklist {
    position: absolute;
    top: 130px; left: 26px; right: 30px;
    list-style: none;
    color: var(--white);
    font-size: 8.6px;
    line-height: 1.35;
  }
  .checklist li {
    position: relative;
    padding-left: 16px;
    margin-bottom: 2px;
  }
  .checklist svg {
    position: absolute;
    left: 0; top: 1px;
    width: 10px; height: 10px;
  }
  .benefits {
    position: absolute;
    top: 232px; left: 26px; right: 26px;
  }
  .benefits__title {
    font-family: "Oswald", sans-serif;
    font-weight: 600;
    font-size: 10.5px;
    color: var(--orange);
    text-transform: uppercase;
    margin-bottom: 6px;
  }
  .benefits__list {
    list-style: disc;
    padding-left: 12px;
    color: var(--text);
    font-size: 8.4px;
    line-height: 1.4;
  }
  .benefits__list li { margin-bottom: 5px; }
  .contact {
    position: absolute;
    bottom: 38px; left: 26px; right: 26px;
    display: flex;
    align-items: center;
    justify-content: flex-end;
    gap: 10px;
    font-family: "Oswald", sans-serif;
    font-weight: 700;
    color: var(--black);
    white-space: nowrap;
  }
  .contact__label { font-size: 20px; }
  .contact__icon { width: 20px; height: 20px; }
  .contact__number { font-size: 26px; color: var(--white); }
</style>
</head>
<body>

<section class="flyer flyer--front">
  <div class="brand">
    <span class="brand__name">Harborline</span>
    <span class="brand__partner">Norvio</span>
  </div>
  <div class="front__rule"></div>
  <div class="front__photo" role="img" aria-label="Photo of a woman working on a laptop at a wooden table in a cafe, with a glass of red wine and a window behind her"></div>
  <h1 class="front__headline">
    <span class="headline__offer">Offer</span>
    <span class="headline__audience">Your Customers</span>
    <span class="headline__wifi">Free WiFi</span>
  </h1>
</section>

<section class="flyer flyer--back">
  <svg class="back__shapes" viewBox="0 0 400 566" preserveAspectRatio="none" aria-hidden="true">
    <polygon points="0,0 400,0 400,92 0,118" fill="#1b1b1b"/>
    <polygon points="0,118 400,92 400,190 0,216" fill="#f39a1e"/>
    <polygon points="0,472 400,432 400,448 0,488" fill="#1b1b1b"/>
    <polygon points="0,488 400,448 400,566 0,566" fill="#f39a1e"/>
  </svg>

  <p class="back__intro">
    <span class="back__title">HARBORLINE</span>
    offers guest and private Wireless network solutions to our restaurant clients and allow them the choice of how they want to set it up.
  </p>

  <ul class="checklist">
    <li><svg viewBox="0 0 10 10"><polyline points="1,5 4,8 9,1" fill="none" stroke="#fff" stroke-width="1.8"/></svg>Installation time is minimal</li>
    <li><svg viewBox="0 0 10 10"><polyline points="1,5 4,8 9,1" fill="none" stroke="#fff" stroke-width="1.8"/></svg>Down time is almost non-existent</li>
    <li><svg viewBox="0 0 10 10"><polyline points="1,5 4,8 9,1" fill="none" stroke="#fff" stroke-width="1.8"/></svg>Customers can be provided with a quality connection because of the fact that the traffic can be shaped to prevent Peer-to-peer downloads and video streaming which would ultimately slow down web browsing and emails.</li>
  </ul>

  <div class="benefits">
    <h2 class="benefits__title">Benefits of Managed WiFi:</h2>
    <ul class="benefits__list">
      <li>Configuration and changes can be made remotely by the administrators irrespective if the device is on or off which means that the device has almost no downtime after the setup has been completed and that the configuration can be changed without hassle.</li>
      <li>By making use of multiple SSID's (wireless networks), the Harborline network and Public network can operate in conjunction without decrementing the staff or patrons.</li>
      <li>With help from the traffic shaping facilities on the router, patrons will not slow each other's connections ever, even if some users are streaming video while others are browsing pictures on social media.</li>
      <li>The router can be managed to set up a splash screen to display upon connection to advertise information such as the operating hours or current specials.</li>
    </ul>
  </div>

  <div class="contact">
    <span class="contact__label">CALL US AT:</span>
    <svg class="contact__icon" viewBox="0 0 24 24" aria-hidden="true">
      <path d="M6.6 10.8c1.4 2.8 3.8 5.1 6.6 6.6l2.2-2.2c.3-.3.7-.4 1-.2 1.1.4 2.3.6 3.6.6.6 0 1 .4 1 1V20c0 .6-.4 1-1 1C10.6 21 3 13.4 3 4c0-.6.4-1 1-1h3.5c.6 0 1 .4 1 1 0 1.3.2 2.5.6 3.6.1.3 0 .7-.2 1z" fill="#fff"/>
    </svg>
    <span class="contact__number">01-55504821</span>
  </div>
</section>

</body>
</html>
```